Bref créative
VOLTAN - Telecommunications consultancy
Full set of stationary designs required
Professional
Maarten Hoekveld
Project engineer
2385 Harborview Crest Drive
Suite 418
Alameda
94732, California
USA
maarten.hoekveld@voltan-example.com
www.voltan-example.com
Require: Business card, Stationary, Envelopes, Invoice, E-mail signature & Notepad.

```html
<!DOCTYPE html>
<html lang="en">
<head>
<meta charset="utf-8">
<title>VOLTAN Stationery Set</title>
<link href="https://fonts.googleapis.com/css2?family=Roboto:wght@400;500;700;900&display=swap" rel="stylesheet">
<style>
  :root {
    --navy: #0d1f5c;
    --blue: #2a4fb8;
    --blue-light: #4f78d6;
    --paper: #ffffff;
    --ink: #333a4a;
    --rule: #c9ced8;
    --muted: #dfe2e8;
    --backdrop: #e8e5df;
  }
  * { box-sizing: border-box; margin: 0; padding: 0; }
  html, body { width: 1200px; height: 384px; overflow: hidden; }
  body {
    position: relative;
    background: var(--backdrop);
    font-family: "Roboto", Arial, sans-serif;
    color: var(--ink);
  }
  .sheet, .card, .envelope {
    position: absolute;
    background: var(--paper);
    overflow: hidden;
    box-shadow: 0 2px 6px rgba(0,0,0,0.18);
  }
  .sheet { top: 29px; width: 228px; height: 343px; }
  .notepad { left: 29px; }
  .fax { left: 300px; }
  .letterhead { left: 576px; }

  .band { position: absolute; left: 0; bottom: 0; width: 100%; }
  .sheet .band { height: 34px; }

  .brand { position: absolute; display: flex; align-items: center; gap: 4px; }
  .brand-mark { width: 9px; height: 9px; background: var(--navy); }
  .brand-name { font-weight: 900; color: var(--navy); letter-spacing: 0.5px; }
  .brand-tagline { position: absolute; font-size: 4px; color: #6a7285; }
  .sheet .brand { left: 12px; top: 14px; }
  .sheet .brand-name { font-size: 15px; }
  .sheet .brand-tagline { left: 12px; top: 33px; }

  .notepad-lines {
    position: absolute; left: 12px; right: 30px; top: 58px; height: 240px;
    background: repeating-linear-gradient(to bottom, transparent 0 15px, var(--rule) 15px 16px);
  }
  .notepad-word {
    position: absolute; right: -22px; top: 210px;
    transform: rotate(-90deg); transform-origin: center;
    font-size: 26px; font-weight: 400; letter-spacing: 3px;
    color: var(--muted);
  }

  .fax-title { position: absolute; left: 12px; top: 64px; font-size: 15px; color: var(--ink); }
  .fax-fields {
    position: absolute; left: 12px; right: 12px; top: 90px;
    display: grid; grid-template-columns: 1fr 1fr; column-gap: 14px; row-gap: 9px;
  }
  .fax-field { display: flex; align-items: flex-end; gap: 4px; font-size: 5px; }
  .fax-field span.line { flex: 1; border-bottom: 0.6px solid #6a7285; height: 6px; }
  .fax-checks {
    position: absolute; left: 12px; right: 12px; top: 152px;
    display: flex; justify-content: space-between; font-size: 4px;
  }
  .fax-checks li { list-style: none; display: flex; align-items: center; gap: 2px; }
  .fax-checks li::before { content: ""; width: 4px; height: 4px; border: 0.6px solid #6a7285; }

  .footer-address {
    position: absolute; left: 0; right: 0; bottom: 42px;
    text-align: center; font-size: 3.6px; line-height: 5px; color: #6a7285;
  }
  .header-address {
    position: absolute; left: 12px; top: 41px;
    font-size: 3.6px; line-height: 5px; color: #6a7285;
  }

  .card { width: 110px; height: 67px; top: 29px; }
  .card-front { left: 869px; }
  .card-front .brand { left: 8px; top: 9px; }
  .card-front .brand-name { font-size: 10px; }
  .card-front .brand-mark { width: 6px; height: 6px; }
  .card-front .brand-tagline { left: 8px; top: 22px; font-size: 3px; }
  .card-person { position: absolute; right: 6px; top: 10px; text-align: left; width: 44px; }
  .card-person .name { font-size: 4.6px; font-weight: 700; color: var(--navy); }
  .card-person .role { font-size: 3.4px; color: #6a7285; }
  .card-contact { position: absolute; left: 8px; top: 32px; font-size: 3px; line-height: 4.2px; color: #6a7285; }
  .card-front .band { height: 13px; }

  .card-back {
    left: 989px;
    background: linear-gradient(135deg, var(--navy) 0%, var(--blue) 70%, var(--blue-light) 100%);
  }
  .card-back .brand { left: 50%; top: 50%; transform: translate(-50%, -50%); }
  .card-back .brand-name { font-size: 15px; color: #ffffff; }
  .card-back .brand-mark { width: 9px; height: 9px; background: #ffffff; }

  .signature { left: 876px; top: 146px; width: 113px; height: 36px; }
  .signature .brand { left: 6px; top: 7px; }
  .signature .brand-name { font-size: 8px; }
  .signature .brand-mark { width: 5px; height: 5px; }
  .signature .card-person { right: 4px; top: 6px; width: 48px; }
  .signature .card-person .name { font-size: 3.8px; }
  .signature .card-person .role { font-size: 3px; line-height: 4px; }
  .signature .band { height: 8px; }

  .envelope { left: 869px; top: 228px; width: 235px; height: 134px; }
  .envelope .brand { left: 12px; top: 12px; }
  .envelope .brand-name { font-size: 12px; }
  .envelope .brand-mark { width: 7px; height: 7px; }
  .envelope .header-address { top: 30px; }
  .envelope .band { height: 48px; }
</style>
</head>
<body>

<svg width="0" height="0" style="position:absolute" aria-hidden="true">
  <defs>
    <linearGradient id="band-fill" x1="0" y1="0" x2="1" y2="0">
      <stop offset="0" stop-color="#0d1f5c"/>
      <stop offset="0.6" stop-color="#2a4fb8"/>
      <stop offset="1" stop-color="#4f78d6"/>
    </linearGradient>
    <symbol id="swoosh" viewBox="0 0 100 30" preserveAspectRatio="none">
      <path d="M0 14 Q50 2 100 10 L100 30 L0 30 Z" fill="url(#band-fill)"/>
      <path d="M0 10 Q50 -1 100 6 L100 8 Q50 1 0 13 Z" fill="#8fa7e4"/>
    </symbol>
  </defs>
</svg>

<section class="sheet notepad" aria-label="Notepad">
  <div class="brand"><span class="brand-mark"></span><span class="brand-name">VOLTAN</span></div>
  <p class="brand-tagline">Telecommunications Consultancy</p>
  <div class="notepad-lines"></div>
  <p class="notepad-word">NOTEPAD</p>
  <svg class="band"><use href="#swoosh" width="100%" height="100%"/></svg>
</section>

<section class="sheet fax" aria-label="Fax cover sheet">
  <div class="brand"><span class="brand-mark"></span><span class="brand-name">VOLTAN</span></div>
  <p class="brand-tagline">Telecommunications Consultancy</p>
  <h1 class="fax-title">FAX</h1>
  <div class="fax-fields">
    <div class="fax-field">To:<span class="line"></span></div>
    <div class="fax-field">From:<span class="line"></span></div>
    <div class="fax-field">Fax:<span class="line"></span></div>
    <div class="fax-field">Date:<span class="line"></span></div>
    <div class="fax-field">Phone:<span class="line"></span></div>
    <div class="fax-field">Pages:<span class="line"></span></div>
    <div class="fax-field">Re:<span class="line"></span></div>
    <div class="fax-field">CC:<span class="line"></span></div>
  </div>
  <ul class="fax-checks">
    <li>Urgent</li><li>For Review</li><li>Please Comment</li><li>Please Reply</li><li>Please Recycle</li>
  </ul>
  <p class="footer-address">2385 Harborview Crest Drive, Suite 418, Alameda, 94732 California, USA<br>T: 510 555 0142 &nbsp; www.voltan-example.com</p>
  <svg class="band"><use href="#swoosh" width="100%" height="100%"/></svg>
</section>

<section class="sheet letterhead" aria-label="Letterhead">
  <div class="brand"><span class="brand-mark"></span><span class="brand-name">VOLTAN</span></div>
  <p class="header-address">2385 Harborview Crest Drive, Suite 418<br>Alameda, 94732 California, USA</p>
  <p class="footer-address">T: 510 555 0142 &nbsp; F: 510 555 0143<br>www.voltan-example.com</p>
  <svg class="band"><use href="#swoosh" width="100%" height="100%"/></svg>
</section>

<section class="card card-front" aria-label="Business card front">
  <div class="brand"><span class="brand-mark"></span><span class="brand-name">VOLTAN</span></div>
  <p class="brand-tagline">Telecommunications Consultancy</p>
  <div class="card-person">
    <p class="name">Maarten Hoekveld</p>
    <p class="role">Project Engineer</p>
  </div>
  <p class="card-contact">2385 Harborview Crest Drive, Suite 418<br>Alameda, 94732 California, USA<br>maarten.hoekveld@voltan-example.com<br>www.voltan-example.com</p>
  <svg class="band"><use href="#swoosh" width="100%" height="100%"/></svg>
</section>

<section class="card card-back" aria-label="Business card back">
  <div class="brand"><span class="brand-mark"></span><span class="brand-name">VOLTAN</span></div>
</section>

<section class="card signature" aria-label="E-mail signature">
  <div class="brand"><span class="brand-mark"></span><span class="brand-name">VOLTAN</span></div>
  <div class="card-person">
    <p class="name">Maarten Hoekveld</p>
    <p class="role">Project Engineer<br>www.voltan-example.com</p>
  </div>
  <svg class="band"><use href="#swoosh" width="100%" height="100%"/></svg>
</section>

<section class="envelope" aria-label="Envelope">
  <div class="brand"><span class="brand-mark"></span><span class="brand-name">VOLTAN</span></div>
  <p class="header-address">2385 Harborview Crest Drive, Suite 418<br>Alameda, 94732 California, USA</p>
  <svg class="band"><use href="#swoosh" width="100%" height="100%"/></svg>
</section>

</body>
</html>
```